Shine Crew

I need a flyer and business cards to hand out at office buildings and country clubs introducing my new auto detailing business, SHINE CREW. Call or text 913-555-0147 for an appointment. Complete auto detailing done at their place or mine, and we offer pick -up and drop-off, if needed. I believe the flyer needs a car on it. Black, blue, and pink are my preferred colors. While you go about your day's business, whether playing 18 holes of golf or putting in 8 hours at the office, we will have your ride shining like a new penny when you're ready to roll!

```html
<!DOCTYPE html>
<html lang="en">
<head>
<meta charset="utf-8">
<title>Shine Crew – Auto Detailing Flyer</title>
<link rel="stylesheet" href="https://fonts.googleapis.com/css2?family=Poppins:ital,wght@0,400;0,600;0,700;0,800;1,700&display=swap">
<style>
  :root {
    --navy: #001a40;
    --navy-light: #022c68;
    --pink: #c600e3;
    --white: #ffffff;
    --black: #000000;
  }
  * { margin: 0; padding: 0; box-sizing: border-box; }
  html, body { width: 848px; height: 1200px; overflow: hidden; background: var(--navy); }
  .flyer {
    position: relative;
    width: 848px;
    height: 1200px;
    background: var(--navy);
    font-family: "Poppins", sans-serif;
    color: var(--white);
    overflow: hidden;
  }
  .brand-mark {
    position: absolute;
    left: 374px; top: 70px;
    width: 100px; height: 100px;
    border-radius: 50%;
    background: var(--pink);
  }
  .brand-name {
    position: absolute;
    top: 198px; left: 0; width: 100%;
    text-align: center;
    font-weight: 800;
    font-size: 84px;
    line-height: 1;
    letter-spacing: -1px;
    color: var(--white);
  }
  .tagline {
    position: absolute;
    top: 312px; left: 0; width: 100%;
    text-align: center;
    font-weight: 700;
    font-size: 44px;
    line-height: 55px;
    letter-spacing: -0.5px;
  }
  .accent { color: var(--pink); }
  .gallery {
    position: absolute;
    top: 456px; left: 0;
    width: 848px; height: 303px;
  }
  .gallery-photo { position: absolute; inset: 0; }
  .photo-paint {
    background: linear-gradient(135deg, #e9d2d6 0%, #a8162a 45%, #5c0d18 100%);
    clip-path: polygon(0 0, 287px 0, 236px 303px, 0 303px);
  }
  .photo-polish {
    background: linear-gradient(135deg, #d9dde2 0%, #6b6e72 45%, #2a2b2e 100%);
    clip-path: polygon(297px 0, 604px 0, 551px 303px, 246px 303px);
  }
  .photo-coating {
    background: linear-gradient(135deg, #c6ccd8 0%, #2d3442 45%, #0b0d12 100%);
    clip-path: polygon(614px 0, 848px 0, 848px 303px, 562px 303px);
  }
  .service-band {
    position: absolute;
    top: 798px; left: 0;
    width: 100%; height: 56px;
    background: var(--pink);
    text-align: center;
    font-weight: 700;
    font-style: italic;
    font-size: 29px;
    line-height: 56px;
    letter-spacing: -0.3px;
  }
  .pitch {
    position: absolute;
    top: 880px; left: 40px; right: 40px;
    text-align: center;
    font-weight: 400;
    font-size: 22.5px;
    line-height: 30px;
  }
  .divider {
    position: absolute;
    top: 1005px; left: 0;
    width: 100%; height: 14px;
    background: var(--black);
  }
  .contact {
    position: absolute;
    top: 1019px; left: 0;
    width: 100%; height: 181px;
    background: var(--navy-light);
    text-align: center;
    font-weight: 800;
    letter-spacing: -1px;
  }
  .contact-line { display: block; font-size: 56px; line-height: 1; padding-top: 28px; }
  .contact-cta { display: block; font-size: 68px; line-height: 1; margin-top: 10px; }
</style>
</head>
<body>
  <main class="flyer">
    <div class="brand-mark" aria-hidden="true"></div>
    <h1 class="brand-name">SHINE CREW</h1>

    <p class="tagline">
      Complete <span class="accent">auto detailing</span> done<br>
      at your place or mine
    </p>

    <section class="gallery">
      <div class="gallery-photo photo-paint" role="img" aria-label="Technician in blue gloves matching paint colour on a red car"></div>
      <div class="gallery-photo photo-polish" role="img" aria-label="Gloved hand machine-polishing a glossy grey car panel"></div>
      <div class="gallery-photo photo-coating" role="img" aria-label="Gloved hand applying ceramic coating to a dark car with an applicator block"></div>
    </section>

    <div class="service-band">WE OFFER PICK -UP AND DROP-OFF, IF NEEDED</div>

    <p class="pitch">
      While you go about your day's business, whether playing 18 holes of golf or putting in 8 hours at the office, we will have your ride shining like a new penny when you're ready to roll!
    </p>

    <div class="divider"></div>

    <footer class="contact">
      <span class="contact-line">Call or text <span class="accent">913-555-0147</span></span>
      <span class="contact-cta">for an appointment</span>
    </footer>
  </main>
</body>
</html>
```